Website Design for Employee Moral and Happiness Company

Looking for a clean website design that explains our features in a step by step manner so our visitors know exactly what our site does before logging in.

The site is called "Velquo". See logo design and video for a sample of style and an overview of what we do.

Target Market(s)

Business owners that are looking to retain employees.

Number of Pages Required

1 page

```html
<!DOCTYPE html>
<html lang="en">
<head>
<meta charset="utf-8">
<title>Velquo – Employee Morale &amp; Happiness</title>
<link rel="stylesheet" href="https://fonts.googleapis.com/css2?family=Poppins:wght@400;500;600;700;800;900&display=swap">
<style>
:root{
  --orange:#ff6a13;
  --beige:#e7ddd3;
  --cream:#f3eee8;
  --navy:#2f3d63;
  --teal:#2aa2b4;
  --ink:#0c0c0c;
  --text:#2b2b2b;
  --white:#ffffff;
  --grey:#6f6f6f;
}
*{box-sizing:border-box;margin:0;padding:0}
html,body{width:1200px;height:5000px;overflow:hidden}
body{position:relative;background:var(--white);font-family:"Poppins",sans-serif;color:var(--text)}
.backdrop{position:absolute;left:0;top:0;width:1200px;height:5000px;z-index:0}
.layer{position:absolute;z-index:1}
.brand{font-family:"Poppins",sans-serif;font-weight:700;color:var(--ink);letter-spacing:-0.5px}
.btn{position:absolute;display:flex;align-items:center;justify-content:center;background:var(--orange);color:var(--white);border-radius:30px;font-weight:700;font-size:14px;letter-spacing:.3px;text-transform:uppercase}
.art{position:absolute}

/* nav */
.site-nav .brand{position:absolute;left:87px;top:14px;font-size:46px;line-height:1.3}
.nav-links{position:absolute;left:493px;top:34px;display:flex;gap:33px;font-size:15px;font-weight:600;color:var(--ink)}
.nav-links .is-active{color:var(--orange)}
.btn-tickets{position:absolute;left:940px;top:18px;width:172px;height:52px;border:2px solid var(--orange);border-radius:30px;display:flex;align-items:center;justify-content:center;font-size:15px;font-weight:700;color:var(--ink)}

/* hero */
.hero-kicker{position:absolute;left:86px;top:268px;font-size:46px;line-height:1;font-weight:700;color:var(--ink)}
.hero-title{position:absolute;left:84px;top:311px;font-size:104px;font-weight:800;color:var(--ink);line-height:1}
.hero-sub{position:absolute;left:87px;top:421px;font-size:27px;line-height:1;color:#444}
.hero-art{left:560px;top:195px;width:555px;height:410px;border-radius:45% 45% 40% 40%/30% 30% 45% 45%;background:linear-gradient(160deg,#8fcbc4 0%,#3e5c9a 55%,#2f3d63 100%);opacity:.9}

/* about */
.about-kicker{position:absolute;left:0;width:1200px;top:947px;text-align:center;font-size:46px;line-height:1;font-weight:700;color:var(--orange)}
.about-title{position:absolute;left:0;width:1200px;top:977px;text-align:center;font-size:76px;line-height:1;font-weight:800;color:var(--ink)}
.about-copy{position:absolute;left:230px;width:740px;top:1057px;text-align:center;font-size:18px;line-height:31px}
.about-art{left:272px;top:1200px;width:660px;height:432px;border-radius:48% 48% 6px 6px;background:linear-gradient(180deg,#2b5486 0%,#2aa2b4 55%,#c9c0b6 100%)}

/* event */
.event-art{left:0;top:1778px;width:578px;height:370px;border-radius:0 14px 14px 0;background:linear-gradient(135deg,#efeae3 0%,#e3dcd2 100%);box-shadow:0 30px 50px rgba(0,0,0,.12)}
.section-kicker{position:absolute;font-size:46px;line-height:1;font-weight:700;color:var(--orange)}
.section-title{position:absolute;font-size:74px;font-weight:800;color:var(--ink);line-height:1}
.section-copy{position:absolute;font-size:18px;line-height:28px}

/* features */
.features-title{position:absolute;left:0;width:1200px;top:2614px;text-align:center;font-size:72px;line-height:1;font-weight:800;color:var(--ink)}
.feature{position:absolute;top:2728px;width:260px;text-align:center}
.feature .art{position:relative;display:block;margin:0 auto;width:150px;height:150px;border-radius:10px}
.feature h3{margin-top:25px;font-size:25px;font-weight:700;line-height:30px;color:var(--ink)}

/* app */
.phone{position:absolute;left:767px;top:3135px;width:250px;height:476px;border:12px solid var(--navy);border-top-width:36px;border-radius:34px;background:var(--cream);box-shadow:0 20px 40px rgba(0,0,0,.15)}
.phone::before{content:"";position:absolute;left:100px;top:-22px;width:32px;height:8px;border-radius:4px;background:var(--teal)}
.phone .brand{position:absolute;left:0;width:100%;top:180px;text-align:center;font-size:42px;line-height:1.2}
.phone .bar{position:absolute;left:85px;top:258px;width:56px;height:8px;border-radius:4px;background:var(--orange)}
.store-badge{position:absolute;top:3559px;width:145px;height:44px;border-radius:22px;background:var(--ink)}

/* news */
.news-title{position:absolute;left:0;width:1200px;top:3782px;text-align:center;font-size:72px;line-height:1;font-weight:800;color:var(--ink)}
.news-card{position:absolute;top:3888px;width:329px;height:372px;background:var(--white);border-radius:12px;overflow:hidden;box-shadow:0 12px 30px rgba(0,0,0,.08)}
.news-card .art{position:relative;display:block;width:100%;height:218px}
.news-date{margin:36px 0 0 38px;font-size:17px;color:var(--orange)}
.news-card h3{margin:6px 38px 0;font-size:23px;font-weight:700;line-height:30px;color:var(--ink)}

/* newsletter */
.newsletter{position:absolute;left:89px;top:4375px;width:1022px;height:175px;border-radius:88px;background:var(--orange)}
.newsletter p{position:absolute;left:60px;top:56px;font-size:27px;font-weight:700;line-height:31px;color:var(--white)}
.newsletter-field{position:absolute;left:570px;top:61px;width:415px;height:54px;border-radius:27px;background:var(--white);display:flex;align-items:center;justify-content:space-between;padding:0 26px;font-size:15px;color:#333}

/* footer */
.footer-brand{position:absolute;left:0;width:1200px;top:4722px;text-align:center;font-size:62px;line-height:1.2;color:var(--white)}
.footer-links{position:absolute;left:0;width:1200px;top:4812px;display:flex;justify-content:center;gap:33px;font-size:15px;font-weight:600;color:var(--white)}
.social{position:absolute;top:4855px;left:508px;display:flex;gap:10px}
.social span{width:38px;height:38px;border-radius:50%;background:#2a2a2a}
.footer-rule{position:absolute;left:89px;top:4935px;width:1022px;height:1px;background:#333}
.copyright{position:absolute;left:89px;top:4962px;font-size:13px;color:var(--white)}
.legal{position:absolute;right:89px;top:4962px;display:flex;gap:18px;font-size:13px;color:var(--white)}
.to-top{position:absolute;left:1125px;top:4925px;width:40px;height:40px;border-radius:50%;background:var(--orange);display:flex;align-items:center;justify-content:center}
</style>
</head>
<body>

<svg class="backdrop" viewBox="0 0 1200 5000" aria-hidden="true">
  <rect x="0" y="0" width="1200" height="1640" fill="#e7ddd3"/>
  <path d="M0 560 C180 700 420 790 700 780 C900 772 1060 700 1200 620 L1200 800 C1000 860 760 880 560 860 C320 836 150 740 0 640 Z" fill="#ece4dc"/>
  <path d="M0 1245 C170 1225 330 1255 470 1340 C560 1395 620 1530 760 1575 C900 1615 1050 1520 1200 1470 L1200 1640 L0 1640 Z" fill="#ffffff"/>
  <path d="M0 1245 C130 1228 240 1240 320 1275" fill="none" stroke="#ff6a13" stroke-width="4"/>
  <path d="M880 1590 C980 1560 1080 1500 1200 1470" fill="none" stroke="#ff6a13" stroke-width="26"/>
  <path d="M0 2430 C200 2440 330 2380 470 2330 C650 2260 800 2100 1000 2190 C1100 2240 1150 2200 1200 2190 L1200 3060 C1100 3140 950 3170 850 3130 C650 3050 550 3000 400 3060 C250 3120 120 3170 0 3150 Z" fill="#e7ddd3"/>
  <path d="M0 4525 C220 4470 420 4500 620 4570 C820 4640 1020 4580 1200 4500 L1200 5000 L0 5000 Z" fill="#0c0c0c"/>
</svg>

<header class="layer site-nav" style="left:0;top:0;width:1200px;height:90px">
  <span class="brand">Velquo</span>
  <nav class="nav-links">
    <span class="is-active">Home</span><span>About us</span><span>Events</span><span>News</span><span>Contact</span>
  </nav>
  <span class="btn-tickets">BUY TICKETS</span>
</header>

<section class="layer hero" style="left:0;top:0;width:1200px;height:700px">
  <p class="hero-kicker">I am here</p>
  <h1 class="hero-title">To Help</h1>
  <p class="hero-sub">Businesses Like Yours</p>
  <span class="btn" style="left:89px;top:467px;width:172px;height:52px">Send Request</span>
  <div class="art hero-art" role="img" aria-label="Illustration of colleagues relaxing on armchairs and chatting"></div>
</section>

<section class="layer about" style="left:0;top:0;width:1200px;height:1640px">
  <p class="about-kicker">About</p>
  <h2 class="about-title brand">Velquo</h2>
  <p class="about-copy">Lorem Ipsum is simply dummy text of the printing and typesetting industry. Lorem Ipsum has been the industry's standard dummy text ever since .</p>
  <span class="btn" style="left:514px;top:1135px;width:172px;height:50px">Read More</span>
  <div class="art about-art" role="img" aria-label="Illustration of a man working on a laptop at a desk with message and calendar icons"></div>
</section>

<section class="layer event" style="left:0;top:1760px;width:1200px;height:420px">
  <div class="art event-art" style="top:18px" role="img" aria-label="Illustration of an event planner dashboard with schedule, messages and task cards"></div>
  <p class="section-kicker" style="left:646px;top:85px">Event</p>
  <h2 class="section-title" style="left:644px;top:129px">Planning</h2>
  <p class="section-copy" style="left:648px;top:216px;width:480px">Lorem Ipsum is simply dummy text of the printing and typesetting industry. Lorem Ipsum has been the industry's standard dummy text ever since .</p>
  <span class="btn" style="left:648px;top:314px;width:172px;height:50px">Register Free</span>
</section>

<section class="layer features" style="left:0;top:0;width:1200px;height:3200px">
  <h2 class="features-title">Our Features</h2>
  <div class="feature" style="left:85px">
    <div class="art" style="background:linear-gradient(160deg,#e9e3da,#4fa7b4)" role="img" aria-label="Illustration of a smiling employee with an ID card"></div>
    <h3>Increase<br>Employee Retention</h3>
  </div>
  <div class="feature" style="left:357px">
    <div class="art" style="background:linear-gradient(160deg,#2f3d63,#ff6a13)" role="img" aria-label="Illustration of a raffle ticket and bid tag"></div>
    <h3>Raffles to<br>Aucations</h3>
  </div>
  <div class="feature" style="left:613px">
    <div class="art" style="background:#2f3d63" role="img" aria-label="Illustration of a cheerful speech bubble"></div>
    <h3>Boost employee<br>Morale</h3>
  </div>
  <div class="feature" style="left:877px">
    <div class="art" style="background:linear-gradient(160deg,#ece6de,#ff8a4a)" role="img" aria-label="Illustration of a photo of happy coworkers"></div>
    <h3>Transform Your<br>Work Events</h3>
  </div>
</section>

<section class="layer app" style="left:0;top:0;width:1200px;height:3700px">
  <p class="section-kicker" style="left:85px;top:3329px">Velquo</p>
  <h2 class="section-title" style="left:82px;top:3374px">Download App</h2>
  <p class="section-copy" style="left:87px;top:3463px;width:570px">Lorem Ipsum is simply dummy text of the printing and typeset-ting industry. Lorem Ipsum has been the industry's standard dummy text ever since .</p>
  <span class="store-badge" style="left:89px" role="img" aria-label="App store download badge"></span>
  <span class="store-badge" style="left:239px" role="img" aria-label="App store download badge"></span>
  <div class="phone">
    <span class="brand">Velquo</span>
    <span class="bar"></span>
  </div>
</section>

<section class="layer news" style="left:0;top:0;width:1200px;height:4300px">
  <h2 class="news-title">Our News &amp; Events</h2>
  <article class="news-card" style="left:87px">
    <div class="art" style="background:linear-gradient(135deg,#2f3d63 0%,#2aa2b4 50%,#e7ddd3 100%)" role="img" aria-label="Illustration of a man working at a computer"></div>
    <p class="news-date">November 27, 201535 Likes</p>
    <h3>FAQ about Friendly Gatherings</h3>
  </article>
  <article class="news-card" style="left:435px">
    <div class="art" style="background:#e7ddd3" role="img" aria-label="Illustration of instant photos of smiling friends"></div>
    <p class="news-date">November 27, 201535 Likes</p>
    <h3>Best Kids' Birthday Party Ideas</h3>
  </article>
  <article class="news-card" style="left:781px">
    <div class="art" style="background:#ff6a13" role="img" aria-label="Illustration of before and after photos of coworkers"></div>
    <p class="news-date">November 27, 201535 Likes</p>
    <h3>Top 10 Afterparty Golden Rules</h3>
  </article>
</section>

<section class="newsletter" style="z-index:1">
  <p>Subscribe to our newsletter to get<br>the latest trends &amp; news</p>
  <div class="newsletter-field">
    <span>Enter your email</span>
    <svg width="20" height="20" viewBox="0 0 20 20" aria-hidden="true"><path d="M2 9 L18 2 L12 18 L9 11 Z" fill="#0c0c0c"/></svg>
  </div>
</section>

<footer class="layer site-footer" style="left:0;top:0;width:1200px;height:5000px">
  <p class="footer-brand brand">Velquo</p>
  <nav class="footer-links"><span>Home</span><span>About us</span><span>Events</span><span>News</span><span>Contact</span></nav>
  <div class="social" aria-label="Social links"><span></span><span></span><span></span><span></span></div>
  <div class="footer-rule"></div>
  <p class="copyright">©Copyright 2022 Velquo | All Rights Reserved</p>
  <p class="legal"><span>Terms &amp; Conditions</span><span>Privacy Policy</span></p>
  <span class="to-top"><svg width="12" height="12" viewBox="0 0 12 12" aria-hidden="true"><path d="M2 8 L6 4 L10 8" fill="none" stroke="#fff" stroke-width="2"/></svg></span>
</footer>

</body>
</html>
```